FLUSH FAIRY the solution to twinkle the smell away...because everyone poops

I need a label for my handmade poop spray. Flush fairy is an organic blend of essential oils that eliminates the odor when you poop. Directions must be on the back of the label : shake well before each use. Spray on the toilet water surface 4-6 times to cover the water before you go. Poop as usual and flush. Safe for all pipes and sewer systems. To order visit my Wovi shop enter flush fairy

Font styles to use
Decorative

Requirements
Must have
• Directions on how to use
Nice to have
• Elegant design label. Product is meant to be kept in the bathroom

```html
<!DOCTYPE html>
<html lang="en">
<head>
<meta charset="utf-8">
<title>Flush Fairy Label</title>
<link rel="stylesheet" href="https://fonts.googleapis.com/css2?family=Arimo:ital,wght@0,400;0,700;1,700&family=Montserrat:wght@800&display=swap">
<style>
  :root {
    --label-yellow: #f6b20c;
    --label-border: #e8861c;
    --ink-white: #ffffff;
    --accent-orange: #f0a010;
    --fill-soft: #f8c64a;
  }
  * { margin: 0; padding: 0; box-sizing: border-box; }
  html, body { width: 1200px; height: 558px; overflow: hidden; background: #ffffff; }
  .label {
    position: relative;
    width: 1200px; height: 558px;
    background: var(--label-yellow);
    border: 8px solid var(--label-border);
    color: var(--ink-white);
    font-family: "Arimo", Arial, sans-serif;
    overflow: hidden;
  }
  .brand-mark {
    position: absolute; left: 150px; top: 56px;
    width: 70px; height: 70px; border-radius: 50%;
    background: var(--ink-white);
  }
  .brand-name {
    position: absolute; left: 0; top: 260px; width: 370px;
    text-align: center;
    font-family: "Montserrat", Arial, sans-serif; font-weight: 800;
    font-size: 50px; letter-spacing: 1px; line-height: 1;
  }
  .brand-banner {
    position: absolute; left: 58px; top: 345px;
    width: 256px; height: 40px;
    background: var(--ink-white);
    clip-path: polygon(0 0, 100% 0, 94% 50%, 100% 100%, 0 100%, 6% 50%);
    color: var(--accent-orange);
    font-size: 24px; line-height: 40px; text-align: center;
  }
  .brand-tagline {
    position: absolute; left: 0; top: 418px; width: 370px;
    text-align: center; font-weight: 700; font-size: 20px;
  }
  .footer-quote {
    position: absolute; top: 514px;
    font-weight: 700; font-style: italic; font-size: 13px;
  }
  .footer-quote--front { left: 128px; }
  .footer-quote--back { left: 712px; }
  .story-vertical {
    position: absolute; left: 378px; top: 30px;
    height: 480px; width: 200px;
    writing-mode: vertical-rl; transform: rotate(180deg);
    font-size: 25px; line-height: 32px; text-align: center;
  }
  .back-panel {
    position: absolute; left: 580px; top: 50px; width: 320px;
    text-align: center; font-size: 15px; line-height: 20px;
  }
  .back-panel h2 {
    margin-top: 20px; font-size: 18px; font-weight: 700; line-height: 22px;
  }
  .back-panel .directions { font-weight: 700; font-size: 15px; line-height: 20px; }
  .steps-art {
    position: absolute; left: 622px; top: 322px;
    width: 180px; height: 190px; border-radius: 6px;
    background: var(--fill-soft);
  }
  .step-note {
    position: absolute; left: 814px; width: 100px;
    font-size: 8px; line-height: 10px; font-weight: 700;
  }
  .story-side {
    position: absolute; width: 108px;
    writing-mode: vertical-rl; transform: rotate(180deg);
    font-size: 15px; line-height: 18px; text-align: center;
  }
  .story-side--top { left: 948px; top: 40px; height: 250px; }
  .story-side--bottom { left: 948px; top: 300px; height: 240px; }
  .check-box {
    position: absolute; left: 1102px;
    width: 62px; height: 56px; background: var(--ink-white);
  }
</style>
</head>
<body>
<main class="label">
  <span class="brand-mark"></span>
  <h1 class="brand-name">FLUSH FAIRY</h1>
  <div class="brand-banner">SAMPLE TEXT</div>
  <p class="brand-tagline">“Lorem ipsum dolor sit amet”</p>
  <p class="footer-quote footer-quote--front">“Lorem ipsum dolor sit amet”</p>

  <p class="story-vertical">Flush fairy is delicate blend of organic essential oils that trap indesrable smell and odors sealing the aromas allowing you to forget about courtesy flushing</p>

  <section class="back-panel">
    <p>Flush fairy is delicate blend of organic essential oils that trap indesrable smell and odors sealing the aromas allowing you to forget about courtesy flushing</p>
    <h2>*DIRECTION FOR USE:</h2>
    <p class="directions">Shake 4-6 times in toilet bowl in corner the water surface before you poop. This will absorb the odors. Flush and you're done it.</p>
  </section>

  <div class="steps-art" role="img" aria-label="Toilet icon with three numbered step circles"></div>
  <p class="step-note" style="top:340px">Shake the bottle well before each use, every single time.</p>
  <p class="step-note" style="top:392px">Spray four to six times over the water before you go.</p>
  <p class="step-note" style="top:452px">Poop as usual, then flush. Safe for all pipes and septic.</p>

  <p class="footer-quote footer-quote--back">“Lorem ipsum dolor sit amet”</p>

  <p class="story-side story-side--top">Flush fairy is delicate blend of organic essential oils that trap indesrable smell and odors sealing the aromas allowing you to forget about courtesy flushing</p>
  <p class="story-side story-side--bottom">Flush fairy is delicate blend of organic essential oils that trap indesrable smell and odors sealing the aromas allowing you to forget about courtesy flushing</p>

  <span class="check-box" style="top:62px"></span>
  <span class="check-box" style="top:132px"></span>
  <span class="check-box" style="top:202px"></span>
</main>
</body>
</html>
```